Kestrel Gardenworks Business Card

An eye catching, yet simple business card that includes;

1. our logo
2. office phone - 5083172946
3. email - kestrelgardenworks@mailbrook.com
4. website - www.kestrelgardenworks.com
5. instagram - @kestrelgardenworksnv

```html
<!DOCTYPE html>
<html lang="en">
<head>
<meta charset="utf-8">
<title>Kestrel Gardenworks Business Card</title>
<link rel="stylesheet" href="https://fonts.googleapis.com/css2?family=Poppins:wght@400;700&display=swap">
<style>
  :root {
    --backdrop: #e4d5c6;
    --card: #ffffff;
    --earth: #9c5c2b;
    --ink: #1e1a1a;
  }
  * { margin: 0; padding: 0; box-sizing: border-box; }
  html, body {
    width: 1200px; height: 1200px; overflow: hidden;
    background: var(--backdrop);
    font-family: "Poppins", sans-serif;
  }
  .card {
    position: absolute; left: 251px; width: 705px; height: 423px;
    background: var(--card); overflow: hidden;
  }
  .card--front { top: 169px; }
  .card--back { top: 616px; }
  .brand-name {
    position: absolute; text-align: center;
    font-family: "Poppins", sans-serif; font-weight: 700;
    color: var(--ink); line-height: 1.05;
  }
  .card--front .brand-name {
    left: 0; right: 0; top: 148px; font-size: 54px;
  }
  .card--back .brand-name {
    left: 28px; width: 220px; top: 160px; font-size: 30px;
  }
  .contact-list {
    position: absolute; left: 315px; top: 135px; list-style: none;
  }
  .contact-item {
    display: flex; align-items: center; gap: 8px;
    height: 24px; margin-bottom: 13.5px;
    font-size: 18.5px; color: var(--earth);
  }
  .contact-icon { width: 20px; height: 20px; flex: none; }
  .ground-band {
    position: absolute; left: 0; right: 0; bottom: 0; height: 100px;
    background: linear-gradient(180deg, #a86634 0%, var(--earth) 100%);
  }
</style>
</head>
<body>
  <section class="card card--front">
    <div class="brand-name">Kestrel<br>Gardenworks</div>
  </section>

  <section class="card card--back">
    <div class="ground-band" role="img" aria-label="Desert landscape scene with hills and cacti"></div>

    <div class="brand-name">Kestrel<br>Gardenworks</div>

    <ul class="contact-list">
      <li class="contact-item">
        <svg class="contact-icon" viewBox="0 0 24 24"><path fill="#9c5c2b" d="M6.6 10.8a15.1 15.1 0 0 0 6.6 6.6l2.2-2.2a1 1 0 0 1 1-.25 11.4 11.4 0 0 0 3.6.57 1 1 0 0 1 1 1V20a1 1 0 0 1-1 1A17 17 0 0 1 3 4a1 1 0 0 1 1-1h3.5a1 1 0 0 1 1 1c0 1.25.2 2.45.57 3.57a1 1 0 0 1-.25 1z"/></svg>
        <span>5083172946</span>
      </li>
      <li class="contact-item">
        <svg class="contact-icon" viewBox="0 0 24 24" fill="none" stroke="#9c5c2b" stroke-width="1.6"><circle cx="12" cy="12" r="10"/><ellipse cx="12" cy="12" rx="4.5" ry="10"/><path d="M2 12h20M4 7h16M4 17h16M12 2v20"/></svg>
        <span>www.kestrelgardenworks.com</span>
      </li>
      <li class="contact-item">
        <svg class="contact-icon" viewBox="0 0 24 24" fill="none" stroke="#9c5c2b" stroke-width="1.6"><rect x="2" y="5" width="20" height="14"/><path d="M2 5l10 8 10-8M2 19l7-7M22 19l-7-7"/></svg>
        <span>kestrelgardenworks@mailbrook.com</span>
      </li>
      <li class="contact-item">
        <svg class="contact-icon" viewBox="0 0 24 24"><rect x="3" y="3" width="18" height="18" rx="4" fill="#9c5c2b"/></svg>
        <span>@kestrelgardenworksnv</span>
      </li>
    </ul>
  </section>
</body>
</html>
```